Trade Show Banner "Brindlequay"

1.7' x 3' vertical banner to complement trade show booth panels (3-panel tabletop booth attached). The word file (attached) is for text and not meant to imply design. We manage homeowner and condo associations that are run by volunteer boards of directors who already have full-time jobs or who may have no training in how to run an organization. It can be highly stressful and not very rewarding. We want this poster/banner to convey that feeling of stress along with a hope for relief and relaxation. Our logo is attached. The full logo is the top one in the file. You may also want to use the triangle (attached) in addition to or instead of the logo. Our corporate fonts are attached. Please let me know if you need additional information or if you feel like there is too much copy or any other thoughts or comments you have.

Target Market(s)

Volunteer boards of directors for homeowner and condo associations--all ages, genders, races, occupations.

Industry/Entity Type

Property Management

Other font styles liked:
• "Copper Lantern" is part of a trademark and should be in Mistral with the green from our logo

Requirements
Must have
• Simple, easy to read, don't clash with booth design
Nice to have
• convey the tension of stress contrasted with the feeling of relaxation and relief.

```html
<!DOCTYPE html>
<html lang="en">
<head>
<meta charset="utf-8">
<title>The Art of Brindlequay for Board Members</title>
<link rel="stylesheet" href="https://fonts.googleapis.com/css2?family=Fira+Sans:ital,wght@0,400;0,500;0,600;1,500&family=Lobster&family=Dancing+Script:wght@600&display=swap">
<style>
  :root {
    --maroon: #6d0f1f;
    --maroon-text: #6a1020;
    --green: #1d6c3b;
    --green-line: #2b7a3e;
    --navy: #1c1f5e;
    --white: #ffffff;
  }
  * { margin: 0; padding: 0; box-sizing: border-box; }
  html, body { width: 1200px; height: 2273px; overflow: hidden; background: var(--white); }
  .banner { position: relative; width: 1200px; height: 2273px; font-family: "Fira Sans", sans-serif; }

  .hero { position: absolute; left: 0; top: 0; width: 1200px; height: 929px; background: var(--maroon); }
  .brand {
    position: absolute; left: 586px; top: 91px; width: 506px; height: 232px;
    background: var(--white); border-radius: 24px;
    display: flex; align-items: center; justify-content: center; gap: 22px;
  }
  .brand-mark { width: 44px; height: 44px; background: var(--maroon); flex: none; }
  .brand-name {
    font-weight: 600; font-size: 40px; line-height: 1.15; color: var(--maroon);
    letter-spacing: 1px; text-transform: uppercase;
  }
  .headline { position: absolute; left: 139px; top: 490px; color: var(--white); }
  .headline-lead { font-weight: 500; font-size: 64px; letter-spacing: 1px; line-height: 1; }
  .headline-title {
    font-family: "Lobster", cursive; font-size: 196px; line-height: 1;
    margin-top: -8px; margin-left: 2px;
  }
  .headline-sub { font-size: 64px; font-weight: 400; line-height: 1; margin-top: -6px; margin-left: 14px; }
  .headline-sub em { font-style: italic; }

  .relief-card {
    position: absolute; border: 3px solid var(--green-line); background: var(--white);
    padding: 26px 24px 0 24px;
  }
  .stress { color: var(--maroon-text); font-weight: 600; font-size: 30px; line-height: 1.38; text-transform: uppercase; }
  .stress-label { text-transform: none; }
  .relief { color: var(--navy); font-size: 34px; line-height: 1.42; margin-top: 6px; }
  .relax { font-family: "Lobster", cursive; color: var(--green); font-size: 46px; }
  .tagline { font-family: "Dancing Script", cursive; color: var(--green); font-size: 30px; }

  .card-workload  { left: 64px;  top: 986px;  width: 519px; height: 241px; }
  .card-issues    { left: 615px; top: 986px;  width: 521px; height: 241px; }
  .card-payments  { left: 64px;  top: 1257px; width: 519px; height: 331px; }
  .card-comms     { left: 615px; top: 1257px; width: 521px; height: 331px; }
  .card-collections { left: 64px; top: 1621px; width: 1072px; height: 292px; }

  .divider { position: absolute; left: 0; top: 1954px; width: 1200px; height: 22px; background: var(--navy); }
  .call-to-action {
    position: absolute; left: 0; top: 1976px; width: 1200px; height: 297px;
    background: var(--green); color: var(--white); text-align: center;
  }
  .cta-lead { font-style: italic; font-weight: 500; font-size: 50px; letter-spacing: 1px; margin-top: 48px; line-height: 1.1; }
  .cta-close { font-family: "Lobster", cursive; font-size: 80px; line-height: 1.2; }
</style>
</head>
<body>
<div class="banner">
  <header class="hero">
    <div class="brand">
      <span class="brand-mark"></span>
      <span class="brand-name">Harlow Crest<br>Management, Inc.</span>
    </div>
    <h1 class="headline">
      <div class="headline-lead">THE ART OF</div>
      <div class="headline-title">Brindlequay</div>
      <div class="headline-sub"><em>for</em> BOARD MEMBERS</div>
    </h1>
  </header>

  <section class="relief-card card-workload">
    <p class="stress"><span class="stress-label">Stress:</span> The board has too much work to do</p>
    <p class="relief"><span class="relax">Relax...</span> and let us do the work.</p>
  </section>
  <section class="relief-card card-issues">
    <p class="stress"><span class="stress-label">Stress:</span> Your community has “issues.”</p>
    <p class="relief"><span class="relax">Relax...</span> and let us give you a <span class="tagline">Copper Lantern.</span></p>
  </section>
  <section class="relief-card card-payments">
    <p class="stress"><span class="stress-label">Stress:</span> Your members cannot pay online.</p>
    <p class="relief"><span class="relax">Relax...</span> we’ll give your members multiple<br>ways to pay.</p>
  </section>
  <section class="relief-card card-comms">
    <p class="stress"><span class="stress-label">Stress:</span> Communication is poor or inconsistent.</p>
    <p class="relief"><span class="relax">Relax...</span> we’ll keep you informed with a robust online portal, chock full of information.</p>
  </section>
  <section class="relief-card card-collections">
    <p class="stress"><span class="stress-label">Stress:</span> Your delinquencies are high.</p>
    <p class="relief"><span class="relax">Relax...</span> as a licensed collection agency, we have developed an effective collections program that works in tandem with your collections attorney. Plus, we can report to the credit bureau!</p>
  </section>

  <div class="divider"></div>
  <footer class="call-to-action">
    <p class="cta-lead">COME IN TO TALK AND START</p>
    <p class="cta-close">Relaxing Today!</p>
  </footer>
</div>
</body>
</html>
```